One page flyer for nonprofit focused IT company

I need a one page flyer (one side of a single 8.5x11 page) with text and graphics. The company logo is already done, and it must appear on the flyer along with other icons and graphics. The final design will be printed on heavy weight glossy paper as a handout and also distributed as a PDF.

The text is provided in an attachment, if it needs to be shortened let me know.

Industry/Entity Type

Information Technology

Requirements
Must have
• some flare (colors, icons or images)
Should not have
• While we work for nonprofits, my company is a FOR PROFIT company.

```html
<!DOCTYPE html>
<html lang="en">
<head>
<meta charset="utf-8">
<title>Northgate Systems – 50 Years of NonProfit IT Services</title>
<link rel="stylesheet" href="https://fonts.googleapis.com/css2?family=Lato:wght@400;700&family=Pathway+Gothic+One&family=Cormorant+Garamond:ital,wght@1,500&display=swap">
<style>
:root{
  --brand-red:#8f1329;
  --deep-red:#7a0f22;
  --ink:#1d1d1d;
  --body-ink:#2a2a2a;
  --charcoal:#333333;
  --page:#ffffff;
  --backdrop:#f4f4f4;
}
*{margin:0;padding:0;box-sizing:border-box}
html,body{width:974px;height:1200px;overflow:hidden;background:var(--backdrop)}
body{font-family:"Lato",sans-serif;color:var(--ink)}
.flyer{position:absolute;left:37px;top:17px;width:900px;height:1166px;background:var(--page);box-shadow:0 6px 18px rgba(0,0,0,.25);overflow:hidden}
.abs{position:absolute}
.header-art{left:0;top:0;width:900px;height:470px}
.brand-name{left:36px;top:66px;width:236px;text-align:center;font-family:"Lato",sans-serif;font-weight:700;font-size:24px;line-height:29px;color:var(--ink)}
.anniv{left:340px;top:62px;width:150px;height:100px;color:#fff;font-family:"Cormorant Garamond",serif;font-style:italic;font-weight:500}
.anniv-num{font-size:92px;line-height:1;position:absolute;left:0;top:0}
.anniv-years{font-size:40px;position:absolute;left:62px;top:10px;line-height:1}
.anniv-of{font-size:22px;position:absolute;left:70px;top:54px}
.title{left:497px;top:92px;font-family:"Pathway Gothic One",sans-serif;color:#fff;font-size:54px;line-height:1;white-space:nowrap}
.hero-photo{left:0;top:169px;width:900px;height:296px}
.intro-heading{left:42px;top:470px;font-size:24px;font-weight:700;color:var(--brand-red);letter-spacing:-.3px}
.intro-text{left:42px;top:500px;width:822px;font-size:16.8px;line-height:21.5px;color:var(--ink)}
.tab{height:30px;color:#fff;font-size:23px;line-height:30px;padding-left:16px;background:var(--brand-red);clip-path:polygon(0 0,100% 0,86% 100%,0 100%)}
.tab-successes{left:42px;top:582px;width:162px}
.tab-solutions{left:423px;top:582px;width:153px}
.item-icon{width:52px;height:54px}
.item-heading{font-size:17px;font-weight:700;color:var(--brand-red);line-height:21px;letter-spacing:-.3px}
.item-text{font-size:13px;line-height:15.9px;color:var(--body-ink);text-align:justify}
.success{left:102px;width:310px}
.solution{left:502px;width:363px}
.footer{left:0;top:1100px;width:900px;height:66px}
.footer-url{left:28px;top:1129px;color:#fff;font-size:16px;font-weight:700}
.footer-contact{left:273px;top:1131px;color:#fff;font-size:13.6px;white-space:nowrap}
.footer-contact b{font-weight:700}
</style>
</head>
<body>
<div class="flyer">

  <svg class="abs header-art" viewBox="0 0 900 470" aria-hidden="true">
    <g fill="var(--brand-red)">
      <rect x="377" y="11" width="523" height="1"/>
      <rect x="373" y="18" width="527" height="1.5"/>
      <rect x="368" y="25" width="532" height="2.5"/>
      <rect x="364" y="33" width="536" height="3"/>
      <rect x="359" y="40" width="541" height="3"/>
      <polygon points="355,46 900,46 900,169 272,169"/>
      <rect x="0" y="169" width="900" height="20"/>
    </g>
  </svg>

  <div class="abs brand-name">Northgate Systems Corporation</div>

  <div class="abs anniv">
    <span class="anniv-num">50</span>
    <span class="anniv-years">Years</span>
    <span class="anniv-of">of</span>
  </div>
  <div class="abs title">NonProfit IT Services</div>

  <svg class="abs hero-photo" viewBox="0 0 900 296" role="img" aria-label="Photograph of a hand touching a tablet surrounded by glowing cloud and security icons">
    <defs>
      <linearGradient id="heroBase" x1="0" y1="0" x2="1" y2="0">
        <stop offset="0" stop-color="#1d2b40"/>
        <stop offset=".5" stop-color="#2f4563"/>
        <stop offset="1" stop-color="#3c5676"/>
      </linearGradient>
      <radialGradient id="heroGlow" cx=".44" cy=".5" r=".22">
        <stop offset="0" stop-color="#ffc9a0"/>
        <stop offset=".4" stop-color="#d7856a" stop-opacity=".7"/>
        <stop offset="1" stop-color="#d7856a" stop-opacity="0"/>
      </radialGradient>
      <linearGradient id="heroFade" x1="0" y1="0" x2="0" y2="1">
        <stop offset=".78" stop-color="#fff" stop-opacity="0"/>
        <stop offset="1" stop-color="#fff"/>
      </linearGradient>
    </defs>
    <rect width="900" height="296" fill="url(#heroBase)"/>
    <rect width="900" height="296" fill="url(#heroGlow)"/>
    <polygon points="0,0 272,0 170,110 0,110" fill="var(--brand-red)"/>
    <g fill="#fff" opacity=".85">
      <rect x="0" y="34" width="230" height="2"/>
      <rect x="0" y="48" width="220" height="2"/>
      <rect x="0" y="62" width="210" height="2"/>
      <rect x="0" y="76" width="200" height="2"/>
      <rect x="0" y="90" width="190" height="2"/>
    </g>
    <rect width="900" height="296" fill="url(#heroFade)"/>
    <g fill="#fff" opacity=".8">
      <rect x="0" y="252" width="900" height="1.5"/>
      <rect x="0" y="260" width="900" height="1.5"/>
      <rect x="0" y="270" width="900" height="2"/>
      <rect x="0" y="280" width="900" height="2"/>
    </g>
  </svg>

  <h1 class="abs intro-heading">An Efficient and Elegant Approach to IT Solution Implementations</h1>
  <p class="abs intro-text">Northgate Systems Corporation has been supporting the Information Systems needs of nonprofits for over 50 years.&nbsp; We continually strive to bring the latest technologies and best practices to nonprofits to drive down the cost of IT while implementing systems that drive revenue.</p>

  <h2 class="abs tab tab-successes">Successes</h2>
  <h2 class="abs tab tab-solutions">Solutions</h2>

  <svg class="abs item-icon" style="left:30px;top:632px" viewBox="0 0 52 54" fill="none" stroke="var(--brand-red)" stroke-width="2" aria-hidden="true">
    <circle cx="26" cy="28" r="11"/><path d="M26 21v14M22 25h6a2 2 0 010 4h-4a2 2 0 000 4h6"/><path d="M10 22h6M8 28h6M10 34h6M36 22h6M38 28h6M36 34h6"/><path d="M40 4v10M36 8l4-4 4 4M12 50V40M8 46l4 4 4-4"/>
  </svg>
  <div class="abs success" style="top:636px">
    <h3 class="item-heading">90% Reduction in Software<br>Development Costs</h3>
    <p class="item-text">Regional Vehicle Dealers League Used Car Guide needed to update its core product they engaged their in-house IT department who estimated the project would take 3 years and cost &nbsp;$3,000,000. RVDL decided to work with Northgate Systems Corporation instead, and the product was released to production in only 9 months at <b>one-tenth of the cost</b>, only $300,000</p>
  </div>

  <svg class="abs item-icon" style="left:30px;top:816px" viewBox="0 0 52 54" fill="none" stroke="var(--brand-red)" stroke-width="2.4" aria-hidden="true">
    <rect x="3" y="38" width="10" height="12"/><rect x="21" y="26" width="10" height="24"/><rect x="39" y="12" width="10" height="38"/><path d="M6 26L22 8M14 8h8v8"/>
  </svg>
  <div class="abs success" style="top:822px">
    <h3 class="item-heading">10x Increase in Membership</h3>
    <p class="item-text">Greenway Paths Alliance needed to move to online membership registration and contracted with Northgate Systems Corporation to build a significant online presence to engage potential members. Through compelling online tools and mobile applications, Greenway Paths has <b>increased membership 10 fold.</b></p>
  </div>

  <svg class="abs item-icon" style="left:28px;top:948px" viewBox="0 0 52 54" fill="none" stroke="var(--brand-red)" stroke-width="2" aria-hidden="true">
    <circle cx="9" cy="10" r="7"/><path d="M16 10h8l6 4 8-2 8 6"/><circle cx="9" cy="42" r="7"/><rect x="20" y="30" width="6" height="20"/><rect x="30" y="24" width="6" height="26"/><rect x="40" y="30" width="6" height="20"/>
  </svg>
  <div class="abs success" style="top:954px">
    <h3 class="item-heading">20% Reduction in Overhead</h3>
    <p class="item-text">The National Council for Equal Voices had antiquated systems in place to manage over 500 chapters across the nation.&nbsp; Northgate Systems Corporation developed online tools to allow communication and management between the local chapters and national headquarters. This eliminated much of the overhead of chapter management, <b>reducing HR costs by 20%.</b></p>
  </div>

  <svg class="abs item-icon" style="left:437px;top:632px" viewBox="0 0 52 54" fill="none" stroke="var(--brand-red)" stroke-width="2" aria-hidden="true">
    <rect x="3" y="4" width="46" height="36" rx="2"/><path d="M20 46h12M26 40v6M9 12l5-4 5 4v8H9zM28 20V10M32 20v-6M36 20v-8M40 20v-4M10 32a4 4 0 108 0a4 4 0 10-8 0M26 34l6-6 4 4 8-8"/>
  </svg>
  <div class="abs solution" style="top:636px">
    <h3 class="item-heading">Web Applications</h3>
    <p class="item-text">With a focus on non-profit websites and web-based applications, NSC helps nonprofits communicate with their members and donors while maximizing online giving and engagement.</p>
  </div>

  <svg class="abs item-icon" style="left:437px;top:716px" viewBox="0 0 52 54" fill="none" stroke="var(--brand-red)" stroke-width="2" aria-hidden="true">
    <rect x="4" y="4" width="38" height="46" rx="4"/><path d="M4 12h38M10 24l4-4 4 4v5h-8zM28 24l4-4 4 4v5h-8zM10 40h8M14 36v8M30 32l8 10 8 2"/>
  </svg>
  <div class="abs solution" style="top:721px">
    <h3 class="item-heading">Mobile Applications</h3>
    <p class="item-text">Northgate Systems Corporation implements mobile applications for phones and tablets to provide direct communications with members and donors enabling real-time, two-way interaction.</p>
  </div>

  <svg class="abs item-icon" style="left:437px;top:802px" viewBox="0 0 52 54" fill="none" stroke="var(--brand-red)" stroke-width="2" aria-hidden="true">
    <circle cx="16" cy="24" r="12"/><path d="M14 36V20h4v16M40 4a6 6 0 016 6c0 3-3 4-3 7h-6c0-3-3-4-3-7a6 6 0 016-6zM30 38h12v12H30zM34 28h10"/>
  </svg>
  <div class="abs solution" style="top:808px">
    <h3 class="item-heading">Systems Integration</h3>
    <p class="item-text">IT applications can get scattered and disconnected.&nbsp; Northgate Systems Corporation has decades of experience integrating these applications into a single cohesive system.</p>
  </div>

  <svg class="abs item-icon" style="left:437px;top:884px" viewBox="0 0 52 54" fill="none" stroke="var(--brand-red)" stroke-width="2" aria-hidden="true">
    <rect x="4" y="6" width="40" height="34" rx="2"/><path d="M4 12h40M12 32v-6M17 32v-10M22 32v-8"/><circle cx="32" cy="30" r="7"/><path d="M37 35l9 9"/>
  </svg>
  <div class="abs solution" style="top:893px">
    <h3 class="item-heading">Business Intelligence and Reporting</h3>
    <p class="item-text">Northgate Systems Corporation can wrestle all of an organization's data into simple executive dashboards and reports.</p>
  </div>

  <svg class="abs item-icon" style="left:437px;top:955px" viewBox="0 0 52 54" fill="none" stroke="var(--brand-red)" stroke-width="2" aria-hidden="true">
    <path d="M14 36H10a8 8 0 010-16 14 14 0 0126-4 10 10 0 016 20h-4M24 46V28M18 34l6-6 6 6"/>
  </svg>
  <div class="abs solution" style="top:961px">
    <h3 class="item-heading">Cloud Migration</h3>
    <p class="item-text">Reduce IT costs by migrating to the latest cloud solutions.</p>
  </div>

  <svg class="abs item-icon" style="left:437px;top:1010px" viewBox="0 0 52 54" fill="none" stroke="var(--brand-red)" stroke-width="2" aria-hidden="true">
    <path d="M12 26H10a8 8 0 010-16 14 14 0 0126-4 10 10 0 016 20"/><circle cx="26" cy="30" r="4"/><circle cx="14" cy="36" r="4"/><circle cx="38" cy="36" r="4"/><path d="M19 44a7 7 0 0114 0M7 50a7 7 0 0114 0M31 50a7 7 0 0114 0"/>
  </svg>
  <div class="abs solution" style="top:1014px">
    <h3 class="item-heading">Member Donor Database</h3>
    <p class="item-text">Northgate Systems Corporation's GiveLedger Member / Donor CRM system is fully customized for each client meeting the unique needs of your organization.</p>
  </div>

  <svg class="abs footer" viewBox="0 0 900 66" aria-hidden="true">
    <polygon points="230,0 900,0 900,66 215,66" fill="var(--brand-red)"/>
    <polygon points="230,0 255,12 240,66 215,66" fill="var(--deep-red)"/>
    <polygon points="0,12 255,12 240,66 0,66" fill="var(--charcoal)"/>
  </svg>
  <div class="abs footer-url">www.northgatesystems.com</div>
  <div class="abs footer-contact">Contact Northgate Systems Corporation at <b>hello@northgatesystems.com</b> or <b>555-014-2270 x118</b></div>

</div>
</body>
</html>
```